TRUCK WRAP DESIGN T&K SUPPLY

Create clean, elegant and attractive design with provided information.
It should include:
--Nice, clean and elegant background( either image hi quality or combination of colors).
--T&K Logo(attached), 555-314-2690, FALWICK COATINGS logo(attached), Established 1926.
-- Building Maintenance Supplies
-- Hardware, paints, plumbing, electrical supplies and janitorial supplies.

All this has to be on Passenger, Driver and Back sides. Logo and phone number on the front of the truck.

Colors

Designer to choose colors to be used in the design.

Requirements
Must have
• Create clean, elegant and attractive design with provided information.
• It should include:
• --Nice, clean and elegant background( either image hi quality or combination of colors).
• --T&K Logo(attached), 555-314-2690, FALWICK COATINGS logo(attached), Established 1926.
• -- Building Maintenance Supplies
• -- Hardware, paints, plumbing, electrical supplies and janitorial supplies.
• All this has to be on Passenger, Driver and Back sides. Logo and phone number on the front of the truck.

```html
<!DOCTYPE html>
<html lang="en">
<head>
<meta charset="utf-8">
<title>T&amp;K Supply Truck Wrap</title>
<link rel="stylesheet" href="https://fonts.googleapis.com/css2?family=Montserrat:ital,wght@0,500;0,600;0,700;0,800;1,600;1,700&display=swap">
<style>
  :root {
    --bg: #8c8c8c;
    --red: #d7282f;
    --yellow: #fff200;
    --black: #1b1b1b;
    --blue: #2e3192;
    --navy: #1d1f5c;
    --white: #ffffff;
  }
  * { margin: 0; padding: 0; box-sizing: border-box; }
  html, body { width: 845px; height: 1200px; overflow: hidden; background: var(--bg); }
  .wrap-sheet { position: relative; width: 845px; height: 1200px; font-family: "Montserrat", sans-serif; }
  .wrap-panel { position: absolute; display: block; }
  .panel-passenger { left: 250px; top: 46px; width: 542px; height: 210px; }
  .panel-driver { left: 46px; top: 398px; width: 542px; height: 210px; }
  .panel-back { left: 90px; top: 782px; width: 297px; height: 200px; }
  .panel-front { left: 477px; top: 748px; width: 290px; height: 88px; }

  .fill-red { fill: var(--red); }
  .fill-yellow { fill: var(--yellow); }
  .fill-black { fill: var(--black); }
  .fill-navy { fill: var(--navy); }
  .headline { font-family: "Montserrat", sans-serif; font-weight: 800; }
  .subline { font-family: "Montserrat", sans-serif; font-weight: 700; fill: var(--black); }
  .brand-name { font-family: "Montserrat", sans-serif; font-weight: 800; fill: var(--navy); }
  .offer-tab-label { font-family: "Montserrat", sans-serif; font-weight: 700; font-style: italic; fill: var(--white); }
  .offer-item { font-family: "Montserrat", sans-serif; font-weight: 600; font-style: italic; fill: var(--blue); }
  .call-label { font-family: "Montserrat", sans-serif; font-weight: 600; fill: var(--yellow); }
  .phone-number { font-family: "Montserrat", sans-serif; font-weight: 700; fill: var(--white); }
  .partner-name { font-family: "Montserrat", sans-serif; font-weight: 600; fill: var(--white); }
  .icon-red { fill: none; stroke: var(--red); stroke-width: 2.4; stroke-linecap: round; stroke-linejoin: round; }
</style>
</head>
<body>
<main class="wrap-sheet">

  <!-- Passenger side panel -->
  <svg class="wrap-panel panel-passenger" viewBox="0 0 677 263" aria-label="Passenger side wrap">
    <defs>
      <linearGradient id="side-bg" x1="0" y1="0" x2="1" y2="1">
        <stop offset="0" stop-color="#ffffff"/><stop offset="1" stop-color="#eceef1"/>
      </linearGradient>
      <linearGradient id="tab-red" x1="0" y1="0" x2="0" y2="1">
        <stop offset="0" stop-color="#e63a3f"/><stop offset="1" stop-color="#b3151c"/>
      </linearGradient>
    </defs>
    <rect width="677" height="263" fill="url(#side-bg)"/>
    <rect width="677" height="4" class="fill-red"/>
    <path d="M375 0 H677 V37 H375 Q362 37 362 24 V13 Q362 0 375 0 Z" fill="url(#tab-red)"/>
    <text class="offer-tab-label" x="385" y="27" font-size="18">WE OFFERS :</text>

    <circle cx="90" cy="42" r="28" class="fill-navy"/>
    <text class="brand-name" x="90" y="88" font-size="13" text-anchor="middle">T&amp;K SUPPLY</text>

    <text class="headline fill-red" x="20" y="137" font-size="48" textLength="245" lengthAdjust="spacingAndGlyphs">BUILDING</text>
    <text class="subline" x="20" y="157" font-size="18" textLength="248" lengthAdjust="spacingAndGlyphs">MAINTENANCE SUPPLIES</text>

    <g class="offer-list">
      <path class="icon-red" d="M374 46 L388 60 M388 46 L374 60"/>
      <text class="offer-item" x="410" y="61" font-size="20">Hardware</text>
      <path class="icon-red" d="M373 93 L383 83 M381 79 L391 75 L387 85"/>
      <text class="offer-item" x="408" y="94" font-size="20">Paints</text>
      <path class="icon-red" d="M370 116 H384 V122 M378 110 V116 M372 110 H384"/>
      <text class="offer-item" x="405" y="127" font-size="20">Plumbing</text>
      <circle class="icon-red" cx="377" cy="153" r="8"/>
      <path class="icon-red" d="M374 150 V156 M380 150 V156"/>
      <text class="offer-item" x="402" y="160" font-size="20">Electrical Supplies</text>
      <path class="icon-red" d="M367 181 H380 V193 H367 Z M373 181 L377 171"/>
      <text class="offer-item" x="398" y="193" font-size="20">Janitorial Supplies</text>
    </g>

    <path class="fill-yellow" d="M0 176 C150 162 300 214 430 222 C560 230 640 210 677 170 V263 H0 Z"/>
    <path class="fill-red" d="M0 183 C150 170 300 222 430 229 C560 236 640 217 677 178 V263 H0 Z"/>
    <path class="fill-black" d="M0 191 C150 180 300 229 430 236 C560 242 640 225 677 187 V263 H0 Z"/>

    <circle cx="37" cy="235" r="18" fill="none" stroke="var(--red)" stroke-width="3"/>
    <path d="M33 224 Q28 235 33 246 L38 244 L37 239 Q35 235 37 231 L38 226 Z" class="fill-red"/>
    <text class="call-label" x="72" y="220" font-size="16">Call Us :</text>
    <text class="phone-number" x="72" y="252" font-size="36" textLength="266" lengthAdjust="spacingAndGlyphs">555-314-2690</text>

    <circle cx="548" cy="249" r="5" class="fill-red"/>
    <text class="partner-name" x="559" y="253" font-size="12">Falwick Coatings</text>
  </svg>

  <!-- Driver side panel -->
  <svg class="wrap-panel panel-driver" viewBox="0 0 677 263" aria-label="Driver side wrap">
    <defs>
      <linearGradient id="side-bg-d" x1="0" y1="0" x2="1" y2="1">
        <stop offset="0" stop-color="#ffffff"/><stop offset="1" stop-color="#eceef1"/>
      </linearGradient>
      <linearGradient id="tab-red-d" x1="0" y1="0" x2="0" y2="1">
        <stop offset="0" stop-color="#e63a3f"/><stop offset="1" stop-color="#b3151c"/>
      </linearGradient>
    </defs>
    <rect width="677" height="263" fill="url(#side-bg-d)"/>
    <rect width="677" height="4" class="fill-red"/>
    <path d="M375 0 H677 V37 H375 Q362 37 362 24 V13 Q362 0 375 0 Z" fill="url(#tab-red-d)"/>
    <text class="offer-tab-label" x="385" y="27" font-size="18">WE OFFERS :</text>

    <circle cx="90" cy="42" r="28" class="fill-navy"/>
    <text class="brand-name" x="90" y="88" font-size="13" text-anchor="middle">T&amp;K SUPPLY</text>

    <text class="headline fill-red" x="20" y="137" font-size="48" textLength="245" lengthAdjust="spacingAndGlyphs">BUILDING</text>
    <text class="subline" x="20" y="157" font-size="18" textLength="248" lengthAdjust="spacingAndGlyphs">MAINTENANCE SUPPLIES</text>

    <g class="offer-list">
      <path class="icon-red" d="M374 46 L388 60 M388 46 L374 60"/>
      <text class="offer-item" x="410" y="61" font-size="20">Hardware</text>
      <path class="icon-red" d="M373 93 L383 83 M381 79 L391 75 L387 85"/>
      <text class="offer-item" x="408" y="94" font-size="20">Paints</text>
      <path class="icon-red" d="M370 116 H384 V122 M378 110 V116 M372 110 H384"/>
      <text class="offer-item" x="405" y="127" font-size="20">Plumbing</text>
      <circle class="icon-red" cx="377" cy="153" r="8"/>
      <path class="icon-red" d="M374 150 V156 M380 150 V156"/>
      <text class="offer-item" x="402" y="160" font-size="20">Electrical Supplies</text>
      <path class="icon-red" d="M367 181 H380 V193 H367 Z M373 181 L377 171"/>
      <text class="offer-item" x="398" y="193" font-size="20">Janitorial Supplies</text>
    </g>

    <path class="fill-yellow" d="M0 176 C150 162 300 214 430 222 C560 230 640 210 677 170 V263 H0 Z"/>
    <path class="fill-red" d="M0 183 C150 170 300 222 430 229 C560 236 640 217 677 178 V263 H0 Z"/>
    <path class="fill-black" d="M0 191 C150 180 300 229 430 236 C560 242 640 225 677 187 V263 H0 Z"/>

    <circle cx="37" cy="235" r="18" fill="none" stroke="var(--red)" stroke-width="3"/>
    <path d="M33 224 Q28 235 33 246 L38 244 L37 239 Q35 235 37 231 L38 226 Z" class="fill-red"/>
    <text class="call-label" x="72" y="220" font-size="16">Call Us :</text>
    <text class="phone-number" x="72" y="252" font-size="36" textLength="266" lengthAdjust="spacingAndGlyphs">555-314-2690</text>

    <circle cx="548" cy="249" r="5" class="fill-red"/>
    <text class="partner-name" x="559" y="253" font-size="12">Falwick Coatings</text>
  </svg>

  <!-- Back panel -->
  <svg class="wrap-panel panel-back" viewBox="0 0 371 250" aria-label="Back wrap">
    <defs>
      <linearGradient id="back-bg" x1="0" y1="0" x2="0.6" y2="1">
        <stop offset="0" stop-color="#cde9f3"/><stop offset="0.55" stop-color="#f4f8e6"/><stop offset="1" stop-color="#f5f3b8"/>
      </linearGradient>
    </defs>
    <rect width="371" height="250" fill="url(#back-bg)"/>
    <circle cx="186" cy="52" r="40" class="fill-navy"/>
    <text class="brand-name" x="186" y="110" font-size="14" text-anchor="middle">T&amp;K SUPPLY</text>
    <text class="headline" x="186" y="155" font-size="44" text-anchor="middle" fill="var(--blue)" textLength="226" lengthAdjust="spacingAndGlyphs">BUILDING</text>
    <text class="subline" x="186" y="174" font-size="19" text-anchor="middle" textLength="262" lengthAdjust="spacingAndGlyphs">MAINTENANCE SUPPLIES</text>
    <path class="fill-yellow" d="M0 180 C120 172 250 192 371 180 V250 H0 Z"/>
    <path class="fill-red" d="M0 185 C120 177 250 197 371 185 V250 H0 Z"/>
    <path class="fill-black" d="M0 192 C120 184 250 203 371 191 V250 H0 Z"/>
    <text class="call-label" x="17" y="233" font-size="19">Call Us :</text>
    <text class="phone-number" x="110" y="233" font-size="33" textLength="244" lengthAdjust="spacingAndGlyphs">555-314-2690</text>
  </svg>

  <!-- Front header panel -->
  <svg class="wrap-panel panel-front" viewBox="0 0 362 110" aria-label="Front header wrap">
    <defs>
      <linearGradient id="front-bg" x1="0" y1="0" x2="1" y2="1">
        <stop offset="0" stop-color="#cde9f3"/><stop offset="0.5" stop-color="#f4f8e6"/><stop offset="1" stop-color="#f5f3b8"/>
      </linearGradient>
    </defs>
    <rect width="362" height="110" fill="url(#front-bg)"/>
    <circle cx="181" cy="24" r="20" class="fill-navy"/>
    <text class="brand-name" x="181" y="58" font-size="10" text-anchor="middle">T&amp;K SUPPLY</text>
    <path class="fill-yellow" d="M0 56 C120 62 250 66 362 56 V110 H0 Z"/>
    <path class="fill-red" d="M0 61 C120 67 250 70 362 61 V110 H0 Z"/>
    <path class="fill-black" d="M0 68 C120 72 250 74 362 66 V110 H0 Z"/>
    <text class="call-label" x="22" y="103" font-size="18">Call Us :</text>
    <text class="phone-number" x="110" y="104" font-size="32" textLength="230" lengthAdjust="spacingAndGlyphs">555-314-2690</text>
  </svg>

</main>
</body>
</html>
```